brisk pelts buisness card design

I need a buisness card that has an orange and red outline a side on antelopes head with long horns.I love the one I found on searchly but it has a watermark see below,would it be possible to have something similar?
There is only one other supplier of skins on the sunshine coast ,very expensive and there are a lot of Australian hides.I can supply
a less expensive choice which is extremly different.

Target Market(s)

home owners family stylists bulk buying anniverary wedding gifts

Industry/Entity Type

Searchly

Contact Information for Business Card

BRISK PELTS
EXOTIC HOMEWARES FOR THE MODERN HOME
MIRANDA 0417263948 bellamoor@examplemail.test
imported from Africa no single product the same

Requirements
Must have
• on front BRISK PELTS large either side of logo
red and orange

ethically produced
Nice to have
• I still have to have more pics of gear set up so just one on back
Should not have
• live animals research shows people dont like to look at animal
no running writing

```html
<!DOCTYPE html>
<html lang="en">
<head>
<meta charset="utf-8">
<title>Brisk Pelts – Business Card</title>
<link rel="stylesheet" href="https://fonts.googleapis.com/css2?family=Roboto:wght@400;500&display=swap">
<style>
  :root {
    --backdrop: #ece9e4;
    --card-white: #ffffff;
    --brand-red: #e3101c;
    --brand-red-deep: #c90712;
    --brand-gold: #f2bf4a;
    --rule-yellow: #f6c200;
    --ink: #1c1c1c;
    --ink-soft: #555555;
    --shadow: rgba(0, 0, 0, 0.18);
  }
  * { box-sizing: border-box; margin: 0; padding: 0; }
  html, body {
    width: 924px;
    height: 1200px;
    overflow: hidden;
    background: var(--backdrop);
  }
  .sheet {
    position: relative;
    width: 924px;
    height: 1200px;
    font-family: "Roboto", Arial, sans-serif;
  }
  .card {
    position: absolute;
    left: 82px;
    width: 760px;
    height: 434px;
    box-shadow: 0 10px 28px var(--shadow);
    overflow: hidden;
  }
  .brand {
    display: flex;
    align-items: center;
  }
  .brand-dot {
    border-radius: 50%;
    flex-shrink: 0;
  }
  .brand-name {
    font-family: "Roboto", Arial, sans-serif;
    font-weight: 500;
    line-height: 1;
    white-space: nowrap;
  }
  .tagline {
    font-family: "Roboto", Arial, sans-serif;
    font-weight: 400;
    white-space: nowrap;
  }

  /* ---------- Back card ---------- */
  .card--back {
    top: 110px;
    background: var(--card-white);
  }
  .back__brand {
    position: absolute;
    top: 70px;
    right: 60px;
    gap: 16px;
  }
  .back__brand .brand-dot {
    width: 44px;
    height: 44px;
    background: var(--rule-yellow);
  }
  .back__brand .brand-name {
    font-size: 54px;
    color: var(--brand-red);
  }
  .back__tagline {
    position: absolute;
    left: 40px;
    top: 196px;
    font-size: 19px;
    color: var(--ink-soft);
  }
  .back__contact {
    position: absolute;
    left: 40px;
    top: 246px;
    display: flex;
    align-items: center;
    gap: 22px;
    font-size: 24px;
    color: var(--ink);
  }
  .contact-item { display: flex; align-items: center; gap: 7px; }
  .contact-icon { width: 22px; height: 22px; fill: var(--ink); }
  .back__rule {
    position: absolute;
    left: 0;
    top: 292px;
    width: 100%;
    height: 6px;
    background: var(--rule-yellow);
  }
  .back__band {
    position: absolute;
    left: 0;
    top: 298px;
    width: 100%;
    height: 136px;
    background: var(--brand-red);
    display: flex;
    align-items: center;
    padding-left: 40px;
  }
  .band-line {
    font-size: 30px;
    color: #ffffff;
    letter-spacing: 0.3px;
  }

  /* ---------- Front card ---------- */
  .card--front {
    top: 650px;
    background: linear-gradient(160deg, var(--brand-red) 0%, var(--brand-red-deep) 100%);
  }
  .front__brand {
    position: absolute;
    left: 70px;
    top: 160px;
    gap: 22px;
  }
  .front__brand .brand-dot {
    width: 62px;
    height: 62px;
    background: var(--brand-gold);
  }
  .front__brand .brand-name {
    font-size: 80px;
    color: var(--brand-gold);
  }
  .front__tagline {
    position: absolute;
    left: 70px;
    bottom: 44px;
    font-size: 22px;
    color: #ffffff;
  }
</style>
</head>
<body>
<main class="sheet">

  <section class="card card--back" aria-label="Business card, contact side">
    <div class="brand back__brand">
      <span class="brand-dot" aria-hidden="true"></span>
      <span class="brand-name">BRISK PELTS</span>
    </div>

    <p class="tagline back__tagline">Exotic homewares for the modern home</p>

    <div class="back__contact">
      <span class="contact-name">Miranda</span>
      <span class="contact-item">
        <svg class="contact-icon" viewBox="0 0 24 24" aria-hidden="true">
          <path d="M6.6 10.8a15.1 15.1 0 0 0 6.6 6.6l2.2-2.2a1 1 0 0 1 1-.25 11.4 11.4 0 0 0 3.6.57 1 1 0 0 1 1 1V20a1 1 0 0 1-1 1A17 17 0 0 1 3 4a1 1 0 0 1 1-1h3.5a1 1 0 0 1 1 1c0 1.25.2 2.45.57 3.57a1 1 0 0 1-.25 1z"/>
        </svg>
        0417263948
      </span>
      <span class="contact-item">
        <svg class="contact-icon" viewBox="0 0 24 24" aria-hidden="true">
          <path d="M2 5h20v14H2z M3.5 6.5v.4l8.5 6 8.5-6v-.4z" fill-rule="evenodd"/>
        </svg>
        bellamoor@examplemail.test
      </span>
    </div>

    <div class="back__rule" aria-hidden="true"></div>
    <div class="back__band">
      <p class="band-line">imported from Africa no single product the same</p>
    </div>
  </section>

  <section class="card card--front" aria-label="Business card, brand side">
    <div class="brand front__brand">
      <span class="brand-dot" aria-hidden="true"></span>
      <span class="brand-name">BRISK PELTS</span>
    </div>
    <p class="tagline front__tagline">Exotic homewares for the modern home</p>
  </section>

</main>
</body>
</html>
```